Business Card Design Project

We would like a business card designed for our Tulip & Acorn Club. Although we do want to be creative, it is important for us to maintain branding, therefore most of the design will be copied from our website.
We do want people to know what it is all about, so we included some of the wording. However we rely heavily on your advice and if you think it is better without then as long as design is good we are willing to consider it.
All designs submitted must follow print-ready design rules. Use only CMYK colours
Target Market(s)
Mothers and mothers-to-be
Industry/Entity Type
Business
Look and feel
Each slider illustrates characteristics of the customer's brand and the style your logo design should communicate.

```html
<!DOCTYPE html>
<html lang="en">
<head>
<meta charset="utf-8">
<title>Tulip &amp; Acorn Club – Business Cards</title>
<link rel="stylesheet" href="https://fonts.googleapis.com/css2?family=Cinzel:wght@400;700&family=Exo+2:wght@700&display=swap">
<style>
  :root {
    --stage: #e7e2da;
    --card-black: #030607;
    --teal-deep: #0d3d4a;
    --teal-mid: #1d6f7c;
    --green-glow: #1f6e58;
    --ink-white: #f4f6f5;
    --panel: rgba(40, 60, 66, 0.55);
    --serif: 'Cinzel', Georgia, serif;
    --sans: 'Exo 2', Arial, sans-serif;
  }
  * { box-sizing: border-box; margin: 0; padding: 0; }
  html, body {
    width: 1200px; height: 926px; overflow: hidden;
    background: var(--stage);
  }
  .sheet { position: relative; width: 1200px; height: 926px; }

  .card {
    position: absolute; top: 118px;
    width: 400px; height: 690px;
    background: var(--card-black);
    color: var(--ink-white);
    overflow: hidden;
    box-shadow: 0 10px 30px rgba(0,0,0,.25);
  }
  .card--front { left: 170px; }
  .card--back  { left: 630px; }

  .card__glow { position: absolute; inset: 0; }
  .card--front .card__glow {
    background:
      radial-gradient(ellipse 60% 30% at 35% 42%, rgba(29,111,124,.75), transparent 70%),
      radial-gradient(ellipse 55% 28% at 25% 70%, rgba(13,61,74,.9), transparent 75%),
      radial-gradient(circle at 85% 22%, rgba(31,110,88,.55), transparent 30%),
      var(--card-black);
  }
  .card--back .card__glow {
    background:
      radial-gradient(ellipse 55% 25% at 40% 35%, rgba(31,110,88,.7), transparent 70%),
      radial-gradient(ellipse 50% 30% at 70% 62%, rgba(29,111,124,.6), transparent 75%),
      radial-gradient(circle at 20% 75%, rgba(31,110,88,.45), transparent 28%),
      var(--card-black);
  }

  .brand {
    position: absolute; top: 52px; left: 0; right: 0;
    display: flex; align-items: center; justify-content: center; gap: 10px;
    font-family: var(--sans); font-weight: 700;
    font-size: 30px; letter-spacing: 1px; color: var(--ink-white);
    text-transform: uppercase;
  }
  .brand__mark { width: 14px; height: 14px; background: var(--ink-white); }

  .tagline {
    position: absolute; top: 228px; left: 20px; right: 20px;
    text-align: center; font-family: var(--serif); font-size: 15px;
    letter-spacing: 2.5px; line-height: 1.6; text-transform: uppercase;
  }

  .panel {
    position: absolute; background: var(--panel);
    font-family: var(--serif); text-transform: uppercase;
  }
  .panel--activities {
    top: 362px; left: 60px; width: 300px; padding: 18px 18px;
    font-size: 14.5px; letter-spacing: 1.5px; line-height: 1.45;
  }
  .activities { list-style: none; }
  .activities__more { text-align: right; margin-top: 4px; }

  .web {
    position: absolute; bottom: 52px; left: 0; right: 0; text-align: center;
    font-family: var(--serif); font-size: 14px; letter-spacing: 3px; font-weight: 700;
  }

  .motto {
    position: absolute; top: 330px; left: 0; right: 0; text-align: center;
    font-family: var(--sans); font-weight: 700; font-size: 27px;
    text-transform: uppercase; letter-spacing: .5px;
  }
  .panel--cities {
    top: 378px; left: 90px; width: 240px; padding: 16px 0;
    text-align: center; font-size: 19px; letter-spacing: 3.5px; line-height: 1.35;
  }
  .cities { list-style: none; }

  .contact {
    position: absolute; bottom: 40px; left: 0; right: 0; text-align: center;
    font-family: var(--serif); font-size: 12.5px; letter-spacing: 1.5px;
    line-height: 1.55; text-transform: uppercase; font-weight: 700;
  }
</style>
</head>
<body>
<main class="sheet">

  <section class="card card--front">
    <div class="card__glow" role="img" aria-label="Soft teal bokeh light background"></div>
    <div class="brand"><span class="brand__mark"></span>Tulip &amp; Acorn Club</div>
    <p class="tagline">For all moms and moms-to-be<br>Companionship and fun starts here!</p>
    <div class="panel panel--activities">
      <ul class="activities">
        <li>- Weekly meet-a-mom group</li>
        <li>- Monthly mom night out!</li>
        <li>- Holiday parties</li>
        <li>- Summer BBQ &amp; beach parties</li>
        <li>- Bi annual flea market</li>
      </ul>
      <p class="activities__more">...and much more!</p>
    </div>
    <p class="web">www.tulipacornclub.com</p>
  </section>

  <section class="card card--back">
    <div class="card__glow" role="img" aria-label="Soft green and teal bokeh light background"></div>
    <div class="brand"><span class="brand__mark"></span>Tulip &amp; Acorn Club</div>
    <h2 class="motto">Where you belong</h2>
    <div class="panel panel--cities">
      <ul class="cities">
        <li>Monaco</li>
        <li>Nice</li>
        <li>Marseille</li>
        <li>Cannes</li>
        <li>Antibes</li>
      </ul>
    </div>
    <address class="contact" style="font-style:normal">
      Email: info@tulipacornclub.com<br>
      www.tulipacornclub.com/community<br>
      www.tulipacornclub.com
    </address>
  </section>

</main>
</body>
</html>
```